Business card design for new eCommerce site focusing on integrity and strong businsess tactics

We need a business card that will stand out and be memorable. Something with color that matches our company logo colors. Think high end version of Dealvine. There are 2 logos provided. The parent company is called Bright Harbor Ventures and we are presenting a new and very exciting eCommerce site called KeenTraders.example.

Target Market(s)

Our target markets are in the Activities, Food and Beverage, Health and Beauty

Industry/Entity Type

Marketing

Contact Information for Business Card

We have 4 members that need cards...I will provide all info to the winner of the design contest
Business Address is
48730 West 61st Avenue, Suite C204
Phoenix AZ 85917

Font styles to use
Serif
Sans Serif

Colors

Designer to choose colors to be used in the design.

Requirements
Must have
• The card must be memorable...should be unique in design but must exude integrity and be playful .
• I have provided several colors or our parent company...please feel free to use which ever
Nice to have
• I will leave this up to you. Feel free to use other images of your choosing that wraps around our client.....Activities, Dining, Health, Beauty
Should not have
• just dont be boring

```html
<!DOCTYPE html>
<html lang="en">
<head>
<meta charset="utf-8">
<title>Bright Harbor Ventures — Business Card</title>
<link href="https://fonts.googleapis.com/css2?family=Arimo:wght@400;700&display=swap" rel="stylesheet">
<style>
  :root {
    --page: #ffffff;
    --card: #0c0c0c;
    --teal: #3c9e98;
    --white: #ffffff;
    --shadow: rgba(0, 0, 0, 0.55);
  }
  * { margin: 0; padding: 0; box-sizing: border-box; }
  html, body {
    width: 1200px; height: 1200px; overflow: hidden;
    background: var(--page);
    font-family: "Arimo", Arial, sans-serif;
  }
  .card {
    position: absolute; left: 224px; width: 770px; height: 462px;
    background: var(--card); overflow: hidden;
    box-shadow: 0 6px 22px var(--shadow);
  }
  .card--front { top: 123px; }
  .card--back { top: 670px; }

  .rule-set { position: absolute; }
  .rule-set--top { left: 0; top: 18px; }
  .rule-set--bottom { right: 0; top: 403px; }
  .rule {
    position: absolute; height: 4px; left: 0;
  }
  .rule-set--top .rule { width: 512px; background: var(--teal); }
  .rule-set--bottom .rule { width: 513px; background: var(--white); left: auto; right: 0; }
  .rule--second { top: 14px; }

  .dots { position: absolute; display: grid; grid-template-columns: repeat(4, 7px); column-gap: 9px; row-gap: 8px; }
  .dots span { width: 7px; height: 6px; display: block; }
  .dots--top { left: 523px; top: 17px; }
  .dots--top span { background: var(--teal); }
  .dots--bottom { left: 190px; top: 401px; }
  .dots--bottom span { background: var(--white); }

  .brand-mark {
    position: absolute; border: 5px solid var(--teal); border-radius: 50%;
    width: 72px; height: 72px;
  }
  .card--front .brand-mark { left: 129px; top: 133px; }
  .card--back .brand-mark { left: 134px; top: 151px; }

  .wordmark {
    position: absolute; color: var(--teal); font-weight: 700;
    text-align: center; line-height: 1;
  }
  .wordmark__name { display: block; letter-spacing: -0.5px; }
  .wordmark__tag { display: block; letter-spacing: 0.45em; margin-right: -0.45em; }

  .card--front .wordmark--main { left: 0; width: 778px; top: 276px; }
  .wordmark--main .wordmark__name { font-size: 40px; }
  .wordmark--main .wordmark__tag { font-size: 17px; margin-top: 4px; }

  .wordmark--small { color: var(--white); left: 528px; width: 210px; top: 358px; }
  .wordmark--small .wordmark__name { font-size: 24px; }
  .wordmark--small .wordmark__tag { font-size: 10px; margin-top: 2px; }

  .card--back .wordmark--main { left: 20px; width: 340px; top: 292px; }

  .wordmark--hero { left: 300px; width: 440px; top: 75px; }
  .wordmark--hero .wordmark__name { font-size: 46px; }
  .wordmark--hero .wordmark__tag { font-size: 22px; margin-top: 6px; }

  .address {
    position: absolute; left: 474px; top: 354px;
    display: flex; align-items: center; gap: 6px;
    color: var(--white); font-size: 14px; line-height: 24px; letter-spacing: 0.3px;
  }
  .address__icon { width: 30px; height: 30px; flex: none; }
</style>
</head>
<body>

<section class="card card--front">
  <div class="rule-set rule-set--top"><div class="rule"></div><div class="rule rule--second"></div></div>
  <div class="dots dots--top"><span></span><span></span><span></span><span></span><span></span><span></span><span></span><span></span></div>

  <div class="brand-mark"></div>
  <div class="wordmark wordmark--main">
    <span class="wordmark__name">Bright Harbor</span>
    <span class="wordmark__tag">ventures</span>
  </div>

  <div class="wordmark wordmark--small">
    <span class="wordmark__name">Bright Harbor</span>
    <span class="wordmark__tag">ventures</span>
  </div>

  <div class="rule-set rule-set--bottom"><div class="rule"></div><div class="rule rule--second"></div></div>
  <div class="dots dots--bottom"><span></span><span></span><span></span><span></span><span></span><span></span><span></span><span></span></div>
</section>

<section class="card card--back">
  <div class="rule-set rule-set--top"><div class="rule"></div><div class="rule rule--second"></div></div>
  <div class="dots dots--top"><span></span><span></span><span></span><span></span><span></span><span></span><span></span><span></span></div>

  <div class="wordmark wordmark--hero">
    <span class="wordmark__name">Bright Harbor</span>
    <span class="wordmark__tag">ventures</span>
  </div>

  <div class="brand-mark"></div>
  <div class="wordmark wordmark--main">
    <span class="wordmark__name">Bright Harbor</span>
    <span class="wordmark__tag">ventures</span>
  </div>

  <div class="address">
    <svg class="address__icon" viewBox="0 0 30 30" aria-hidden="true">
      <circle cx="15" cy="15" r="13" fill="none" stroke="#ffffff" stroke-width="2.5"/>
      <path d="M7.5 15.5 L15 8.5 L22.5 15.5" fill="none" stroke="#ffffff" stroke-width="2.2" stroke-linejoin="round"/>
      <path d="M10 14 V21 H13.5 V17.5 H16.5 V21 H20 V14 L15 9.5 Z" fill="#ffffff"/>
    </svg>
    <p>48730 West 61st Avenue,<br>Suite C204 Phoenix AZ 85917</p>
  </div>

  <div class="rule-set rule-set--bottom"><div class="rule"></div><div class="rule rule--second"></div></div>
  <div class="dots dots--bottom"><span></span><span></span><span></span><span></span><span></span><span></span><span></span><span></span></div>
</section>

</body>
</html>
```